Bamboo & Ember Business Card FUN & EXCITING

Here is the Information for the Card:
Harpreet Kalra (Toby)
E: TobyKalra@mailbox-demo.com
C: (480) 555-0147
www.BambooEmberLV.com

We don't want traditional Indian cliche, We a playful bold and fun business card.

Files: https://files.sharebox-demo.net/folders/7QtpLmzR2xVbN4kHs9wYcDfJ3eGaUoPi

https://files.sharebox-demo.net/folders/5ZrqTwyX8mKcE2vBn6aLpHsQ9uFjRgOe

Target Market(s)

Las Vegas Local Restaurant

Industry/Entity Type

Indian Restaurant

Contact Information for Business Card

Name, Email, Cell Phone, Company Logo

```html
<!DOCTYPE html>
<html lang="en">
<head>
<meta charset="utf-8">
<title>Bamboo &amp; Ember — Business Card</title>
<link rel="stylesheet" href="https://fonts.googleapis.com/css2?family=Open+Sans:wght@400;700;800&display=swap">
<style>
  :root {
    --stage: #2b2d30;
    --pink: #e01a5f;
    --white: #ffffff;
    --peach: #f6c3a4;
    --peach-soft: #f9d8c4;
    --teal: #1aa58a;
    --gold: #f6b92b;
    --ink: #4a4a4a;
  }
  * { box-sizing: border-box; margin: 0; padding: 0; }
  html, body { width: 1200px; height: 952px; overflow: hidden; }
  body {
    background: var(--stage);
    font-family: "Open Sans", Arial, sans-serif;
    display: flex; flex-direction: column; align-items: center; justify-content: center;
    gap: 32px;
  }
  .card {
    position: relative;
    width: 760px; height: 434px;
    overflow: hidden;
    box-shadow: 0 10px 30px rgba(0,0,0,.45);
  }
  .band { position: absolute; left: 0; width: 100%; }
  .pattern-row { position: absolute; left: 0; width: 100%; height: 16px; }

  /* Contact side */
  .card--front { background: var(--white); }
  .card--front .band { height: 52px; background: var(--pink); }
  .card--front .band--top { top: 0; }
  .card--front .band--bottom { bottom: 0; }
  .card--front .pattern-row { background: var(--peach-soft); }
  .card--front .pattern-row--top { top: 60px; }
  .card--front .pattern-row--bottom { bottom: 60px; }

  .front-body {
    position: absolute; inset: 86px 40px 86px 40px;
    display: flex; flex-direction: column; align-items: center; justify-content: center;
  }
  .wordmark {
    display: flex; align-items: center; gap: 12px;
    font-weight: 800; color: var(--pink);
    letter-spacing: .5px; text-transform: uppercase;
  }
  .wordmark__dot { border-radius: 50%; background: var(--gold); flex: none; }
  .card--front .wordmark { font-size: 40px; }
  .card--front .wordmark__dot { width: 22px; height: 22px; }

  .person {
    margin-top: 30px;
    font-size: 30px; font-weight: 700; color: var(--teal);
    text-transform: uppercase; letter-spacing: .5px;
  }
  .contact-list {
    list-style: none; margin-top: 22px;
    display: flex; gap: 28px;
    font-size: 15px; color: var(--ink);
  }
  .contact-list li { display: flex; align-items: center; gap: 7px; }
  .contact-icon {
    width: 17px; height: 17px; border-radius: 3px; background: var(--gold);
    display: flex; align-items: center; justify-content: center; flex: none;
  }

  /* Logo side */
  .card--back { background: var(--white); }
  .card--back .panel {
    position: absolute; left: 0; top: 48px; width: 100%; height: 338px;
    background: var(--pink);
  }
  .card--back .pattern-row { background: #ef5a8a; }
  .card--back .pattern-row--top { top: 56px; }
  .card--back .pattern-row--bottom { bottom: 56px; }
  .back-body {
    position: absolute; inset: 0;
    display: flex; align-items: center; justify-content: center;
  }
  .card--back .wordmark { color: var(--white); font-size: 52px; }
  .card--back .wordmark__dot { width: 28px; height: 28px; }
</style>
</head>
<body>

  <section class="card card--front" aria-label="Business card, contact side">
    <div class="band band--top"></div>
    <div class="pattern-row pattern-row--top" role="img" aria-label="Row of peach scalloped ornaments"></div>
    <div class="front-body">
      <div class="wordmark"><span class="wordmark__dot"></span>Bamboo &amp; Ember</div>
      <p class="person">Harpreet Kalra (Toby)</p>
      <ul class="contact-list">
        <li>
          <span class="contact-icon">
            <svg width="11" height="11" viewBox="0 0 24 24"><path fill="#fff" d="M6.6 10.8a15 15 0 0 0 6.6 6.6l2.2-2.2c.3-.3.7-.4 1-.2 1.1.4 2.3.6 3.6.6.6 0 1 .4 1 1V20c0 .6-.4 1-1 1A17 17 0 0 1 3 4c0-.6.4-1 1-1h3.5c.6 0 1 .4 1 1 0 1.3.2 2.5.6 3.6.1.3 0 .7-.2 1z"/></svg>
          </span>(480) 555-0147
        </li>
        <li>
          <span class="contact-icon">
            <svg width="11" height="11" viewBox="0 0 24 24"><path fill="none" stroke="#fff" stroke-width="2.4" d="M3 6h18v12H3z M3 6l9 7 9-7"/></svg>
          </span>TobyKalra@mailbox-demo.com
        </li>
        <li>
          <span class="contact-icon">
            <svg width="11" height="11" viewBox="0 0 24 24"><circle cx="12" cy="12" r="8" fill="none" stroke="#fff" stroke-width="2.4"/><path d="M4 12h16M12 4c3 3 3 13 0 16M12 4c-3 3-3 13 0 16" fill="none" stroke="#fff" stroke-width="1.8"/></svg>
          </span>www.BambooEmberLV.com
        </li>
      </ul>
    </div>
    <div class="pattern-row pattern-row--bottom" role="img" aria-label="Row of peach scalloped ornaments"></div>
    <div class="band band--bottom"></div>
  </section>

  <section class="card card--back" aria-label="Business card, logo side">
    <div class="panel"></div>
    <div class="pattern-row pattern-row--top" role="img" aria-label="Row of light pink scalloped ornaments"></div>
    <div class="pattern-row pattern-row--bottom" role="img" aria-label="Row of light pink scalloped ornaments"></div>
    <div class="back-body">
      <div class="wordmark"><span class="wordmark__dot"></span>Bamboo &amp; Ember</div>
    </div>
  </section>

</body>
</html>
```